Psychologist in Private Practice Needs a Website Update

Project Description:
Hello talented designers! My current website, www.jodelbrisk.com, needs a fresh, boho-modern makeover that highlights the warm, welcoming nature of my holistic therapy practice. I want a website that has a serene, boho- modern design, appealing to clients seeking individual therapy, couples therapy, and family counseling.

I’d also like to prepare for a future second site focused exclusively on couples and family therapy. Both sites should be interconnected, so I’m looking for design suggestions that seamlessly link them together while maintaining a cohesive brand look and feel.

Key Objectives:

Boho-Modern Aesthetic: Incorporate natural textures, neutral or earthy tones, and clean lines that capture a modern, inviting vibe.

Responsive Design: Ensure the website is user-friendly on desktop, tablet, and mobile devices.

Clear Service Offerings: Prominently feature my three distinct services: individual therapy, couples therapy, and family counseling.

Interlinked Future Site: Provide ideas on how to cross-link this site with a second site focused on couples and family therapy.

User Experience (UX): Make the site simple to navigate, with intuitive placement of content that speaks to potential clients’ needs.

SEO-Friendly: Implement best practices for structure, site speed, and keyword usage to boost online visibility.

What I Have Now:
Existing website: www.jodelbrisk.com
Basic content and a logo that can be refined or updated to match the boho-modern feel
Rough style guide with brand elements open to a fresh interpretation

Preferred Style/Tone:
Boho-modern with earthy tones, subtle textures, and clean typography
Warm, empathetic, and approachable to align with the nature of therapy services
Slightly artistic or organic elements that evoke calm and connection

Potential for an ongoing design relationship!
Updates

Need extra days to review

Target Market(s)

I have a high functioning, professional clientele who doctors, lawyers, and leaders in their field.

Industry/Entity Type

healthcare/mental health

Coding

Coded - Design and coding required

Font styles to use
Other font styles liked:
• cormorant garamond for headers and Source Sans Pro for supporting text

Colors

Designer to choose colors to be used in the design.

Requirements
Must have
• Open, Harmonious Layout I’d like the overall design to feel upscale, humanistic, open and harmonious, with minimal divisions of space. Rather than traditional section dividers, please consider using images, subtle shifts in color, typography, or spacing to define sections. Hero Image & Inspiration Ideally, the first (hero) image should evoke a sense of awe or inspiration. Focus on simplicity and elegance so the design feels spacious and inviting, allowing the content and imagery to really stand out. Natural Flow Wherever possible, let the design elements flow naturally into each other, creating a sense of unity and cohesion throughout the site.
Nice to have
• 1. Full-Width Hero Image: • The homepage should feature a full-width hero image that extends edge-to-edge across the screen for a modern and visually immersive effect. • This image should set the tone for the website, reflecting a calming, humanistic/natural, and upscale feel. It could include subtle overlays or gradients to enhance readability of text and navigation elements. Ideally, this image should have one or two people in nature. The image could be slightly transparent to allow the text "holistic therapy" and the tagline "an integrative approach to transformation" to be easily visible. Please help me find a breath-taking image that evokes a sense of beauty, inspiration, awe or hope. 2. Menu Tabs Positioned Over the Image: • The menu tabs (navigation bar) should be positioned directly on top of the hero image, either centered or aligned to the top right/left, depending on the design. • The navigation bar should have a slightly transparent or solid background (depending on the image and visibility needs) to ensure the text is easily readable without detracting from the image. 3. Typography and Text Placement: • The text overlay on the hero image should use the selected fonts: • Cormorant Garamond for headers (e.g., the tagline or welcome message). • Source Sans Pro for any supporting text. 5. Seamless Transitions: • Below the full-width image, transitions into the next sections (like “About,” “Services,” or client-focused content) should be smooth, using full-width separators that maintain the cohesive, open layout style. 6. Color Palette: • A neutral and calming color palette should be used (e.g., soft blues, grays, whites, or very muted earth tones) to create a soothing atmosphere for visitors. This design approach ensures the homepage looks clean, modern, and professional while maintaining the calming and upscale aesthetic that reflects the values of my psychology practice

```html
<!DOCTYPE html>
<html lang="en">
<head>
<meta charset="utf-8">
<title>Dr. Jodel Brisk Website Showcase</title>
<link rel="stylesheet" href="https://fonts.googleapis.com/css2?family=Cormorant+Garamond:ital,wght@0,400;0,500;0,600;1,400;1,500&family=Source+Sans+3:wght@300;400;600&display=swap">
<style>
:root{
  --stage:#759b60;
  --page:#1f3b32;
  --olive:#7d9b3e;
  --olive-soft:#9bb35a;
  --cream:#f4efe4;
  --muted:#b9c4bb;
  --ink:#1f3b32;
  --photo-warm:#c9a58a;
  --photo-light:#e4d9cc;
  --serif:"Cormorant Garamond", Georgia, serif;
  --sans:"Source Sans 3", Arial, sans-serif;
}
*{box-sizing:border-box;margin:0;padding:0}
html,body{width:1200px;height:800px;overflow:hidden}
body{background:var(--stage);position:relative;font-family:var(--sans);color:var(--cream)}
h1,h2,h3,p{font-weight:400}
.abs{position:absolute}

.showcase-title{position:absolute;left:0;top:70px;width:1200px;text-align:center;font-family:var(--serif);font-weight:500;font-size:62px;line-height:58px;color:var(--cream)}
.showcase-title .dark{color:var(--ink)}

.page{position:absolute;background:var(--page);overflow:hidden}
.page--left{left:87px;top:233px;width:299px;height:567px}
.page--home{left:423px;top:312px;width:353px;height:488px}
.page--right{left:814px;top:233px;width:300px;height:567px}

.section-title{position:absolute;width:100%;text-align:center;font-family:var(--serif);font-weight:400;font-size:14px;color:var(--cream)}
.section-title em{color:var(--olive-soft)}
.section-sub{position:absolute;width:100%;text-align:center;font-size:3.4px;color:var(--muted)}

.arch{position:absolute;border-radius:999px;overflow:hidden}
.photo{position:absolute}
.tone-a{background:linear-gradient(160deg,var(--photo-light),var(--photo-warm) 55%,#3d3b3a)}
.tone-b{background:linear-gradient(170deg,#e9e2da,var(--photo-warm) 50%,#2f3a3c)}
.tone-c{background:linear-gradient(160deg,#f1ece4,#cdb8a3 50%,#7d8a8a)}

.service-label{position:absolute;text-align:center;font-size:5.2px;color:var(--cream)}
.service-label em{font-style:normal;color:var(--olive-soft)}
.service-copy{position:absolute;text-align:center;font-size:3.2px;line-height:4.2px;color:var(--muted)}
.learn-more{position:absolute;font-family:var(--serif);font-size:5px;color:var(--cream);border-bottom:.5px solid var(--cream);padding-bottom:1px}

.slogan{position:absolute;font-family:var(--sans);font-weight:400;line-height:1.02;color:var(--cream);text-transform:uppercase;white-space:nowrap}
.portrait{position:absolute;border-radius:50%;background:radial-gradient(circle at 50% 40%,#e2b79c 0 25%,#a8724f 45%,#5b3b2c 75%)}
.portrait-back{position:absolute;border-radius:50%;background:var(--olive)}

.nav{position:absolute;top:14px;left:18px;right:18px;display:flex;justify-content:space-between;align-items:center;font-size:4.6px;text-transform:uppercase;color:var(--cream)}
.nav .brand{font-family:var(--serif);font-weight:400;font-size:9px;text-transform:none;color:var(--cream)}
.eyebrow{position:absolute;font-size:3.2px;letter-spacing:.3px;color:var(--olive-soft)}
.hero-title{position:absolute;font-family:var(--serif);font-weight:400;font-size:13.5px;line-height:15px;color:var(--cream)}
.hero-title .accent{color:var(--olive-soft)}
.hero-title i{font-weight:500}
.hero-copy{position:absolute;font-size:3.6px;line-height:5px;color:var(--muted)}
.btn{position:absolute;background:var(--olive);border-radius:20px;color:var(--cream);font-size:3.4px;display:flex;align-items:center;justify-content:center;text-transform:uppercase}

.faq-eyebrow{position:absolute;width:100%;text-align:center;font-size:3.4px;color:var(--muted)}
.faq-title{position:absolute;width:100%;text-align:center;font-size:8px;line-height:11px;color:var(--cream)}
.faq-row{position:absolute;left:84px;width:134px;height:18px;border-bottom:.6px solid #7b8f84;font-size:3.4px;color:var(--cream);display:flex;justify-content:space-between;align-items:center}
.ticker{position:absolute;left:0;top:319px;width:300px;white-space:nowrap;font-size:8.6px;color:var(--cream);text-transform:uppercase}
.ticker .serif{font-family:var(--serif);font-size:9.4px}
.ticker .star{color:var(--olive-soft);margin:0 4px}
.join{position:absolute;width:100%;text-align:center;font-size:10px;line-height:12px;color:var(--cream)}
</style>
</head>
<body>

<h1 class="showcase-title">Dr. Jodel Brisk <span class="dark">Website</span><br><span class="dark">Showcase</span></h1>

<!-- Services and slogan page -->
<section class="page page--left">
  <h2 class="section-title" style="top:20px">What We <em>Offer</em></h2>
  <p class="section-sub" style="top:41px">are you struggling with issues that affect the way you live, love or work?</p>

  <div class="arch tone-a" style="left:39px;top:54px;width:71px;height:102px" role="img" aria-label="Photo of a woman in an individual therapy session"></div>
  <div class="arch tone-b" style="left:115px;top:54px;width:71px;height:102px" role="img" aria-label="Photo of a couple talking with a therapist"></div>
  <div class="arch tone-c" style="left:190px;top:54px;width:72px;height:102px" role="img" aria-label="Photo of a family in a counselling session"></div>

  <p class="service-label" style="left:39px;top:163px;width:71px">Individual <em>Therapy</em></p>
  <p class="service-label" style="left:115px;top:163px;width:71px">Couples <em>Therapy</em></p>
  <p class="service-label" style="left:190px;top:163px;width:72px"><em>Family</em> Counselling</p>
  <p class="service-copy" style="left:39px;top:172px;width:71px">Calm, private sessions shaped around your goals and pace.</p>
  <p class="service-copy" style="left:115px;top:172px;width:71px">Rebuild trust and connection together with guided support.</p>
  <p class="service-copy" style="left:190px;top:172px;width:72px">Help every voice at home be heard and understood.</p>
  <span class="learn-more" style="left:135px;top:202px">Learn More →</span>

  <div class="photo" style="left:0;top:240px;width:102px;height:124px;background:linear-gradient(180deg,#dfe3e0,#c8b28d 70%,#8c7a55)" role="img" aria-label="Photo of a woman with open arms on a hillside"></div>
  <div class="photo" style="left:102px;top:240px;width:103px;height:124px;background:linear-gradient(180deg,#e8d7c2,#b79a78 55%,#5e5a3a)" role="img" aria-label="Photo of a couple sitting together on a hill at sunset"></div>
  <div class="photo" style="left:205px;top:240px;width:94px;height:124px;background:linear-gradient(160deg,#cfe0c0,#8fa85e 50%,#d7c0a6)" role="img" aria-label="Photo of a laughing family lying in the grass"></div>

  <div class="portrait-back" style="left:26px;top:396px;width:108px;height:140px"></div>
  <div class="portrait" style="left:17px;top:398px;width:108px;height:141px" role="img" aria-label="Portrait photo of the therapist"></div>
  <svg class="abs" style="left:150px;top:430px" width="140" height="90" viewBox="0 0 140 90" aria-hidden="true">
    <path d="M10 60 Q70 30 132 32" fill="none" stroke="#3f5e4c" stroke-width="5" stroke-linecap="round"/>
    <text x="57" y="12" fill="#9bb35a" font-size="9">*</text>
  </svg>
  <p class="slogan" style="left:138px;top:431px;font-size:24px"><span style="margin-left:12px">Stay</span><br>Mentally<br><span style="margin-left:12px">Strong</span></p>
</section>

<!-- Home page -->
<section class="page page--home">
  <nav class="nav">
    <span>Home</span><span>Services</span><span>About</span>
    <span class="brand">Dr. Jodel Brisk</span>
    <span>FAQs</span><span>Blog</span><span>Contact</span>
  </nav>
  <p class="eyebrow" style="left:32px;top:58px">ARE YOU READY FOR THE TRANSFORMATION?</p>
  <h2 class="hero-title" style="left:32px;top:67px">Holistic <span class="accent">Therapy</span>, An<br><i>Integrative</i> Approach To<br><span class="accent">Transformation.</span></h2>
  <p class="hero-copy" style="left:32px;top:120px;width:122px">We have extensive experience treating a full spectrum of mental health disorders using a collaborative and compassionate approach.</p>
  <span class="btn" style="left:32px;top:140px;width:63px;height:19px">Contact us now</span>
  <div class="abs" style="left:177px;top:186px;width:1px;height:21px;background:#4f6a5c"></div>

  <svg class="abs" style="left:214px;top:44px" width="70" height="140" viewBox="0 0 70 140" aria-hidden="true">
    <path d="M0 140 V40 Q0 0 40 0 Q62 0 70 20 V140 H0Z" fill="var(--olive)"/>
  </svg>
  <div class="arch" style="left:229px;top:61px;width:124px;height:116px;border-radius:46px 46px 0 0;background:linear-gradient(150deg,#f2e6d2,#c99b6d 45%,#3f3a36)" role="img" aria-label="Photo of friends smiling together in warm light"></div>
  <svg class="abs" style="left:277px;top:123px" width="76" height="75" viewBox="0 0 76 75" aria-hidden="true">
    <path d="M8 70 Q0 25 30 5 Q70 20 76 70Z" fill="var(--olive-soft)"/>
  </svg>

  <h2 class="section-title" style="top:239px">What We <em>Offer</em></h2>
  <div class="arch tone-a" style="left:46px;top:279px;width:84px;height:118px" role="img" aria-label="Photo of a woman in an individual therapy session"></div>
  <div class="arch tone-b" style="left:135px;top:279px;width:84px;height:118px" role="img" aria-label="Photo of a couple talking with a therapist"></div>
  <div class="arch tone-c" style="left:224px;top:279px;width:84px;height:118px" role="img" aria-label="Photo of a family in a counselling session"></div>

  <p class="service-label" style="left:46px;top:405px;width:84px"><em>Individual</em> Therapy</p>
  <p class="service-label" style="left:135px;top:405px;width:84px"><em>Couples</em> Therapy</p>
  <p class="service-label" style="left:224px;top:405px;width:84px"><em>Family</em> Counseling</p>
  <p class="service-copy" style="left:46px;top:414px;width:84px">Calm, private sessions shaped around your goals and pace.</p>
  <p class="service-copy" style="left:135px;top:414px;width:84px">Rebuild trust and connection together with guided support.</p>
  <p class="service-copy" style="left:224px;top:414px;width:84px">Help every voice at home be heard and understood.</p>
  <span class="learn-more" style="left:160px;top:450px">Learn More →</span>
</section>

<!-- FAQ and community page -->
<section class="page page--right">
  <div class="portrait-back" style="left:30px;top:-4px;width:118px;height:140px"></div>
  <div class="portrait" style="left:18px;top:-2px;width:108px;height:138px" role="img" aria-label="Portrait photo of the therapist"></div>
  <svg class="abs" style="left:140px;top:20px" width="160" height="80" viewBox="0 0 160 80" aria-hidden="true">
    <path d="M20 60 Q90 35 150 35" fill="none" stroke="#3f5e4c" stroke-width="5" stroke-linecap="round"/>
    <text x="66" y="12" fill="#9bb35a" font-size="9">*</text>
  </svg>
  <p class="slogan" style="left:138px;top:28px;font-size:24px"><span style="margin-left:13px">Stay</span><br>Mentally<br><span style="margin-left:13px">Strong</span></p>

  <p class="faq-eyebrow" style="top:162px">FAQ</p>
  <p class="faq-title" style="top:172px">Frequently asked questions<br>about Dr. Jodel Therapy</p>
  <div class="faq-row" style="top:201px"><span>Lorem ipsum dolor sit amet consectetur?</span><span>+</span></div>
  <div class="faq-row" style="top:220px"><span>Lorem ipsum dolor sit amet consectetur?</span><span>+</span></div>
  <div class="faq-row" style="top:239px"><span>Lorem ipsum dolor sit amet consectetur?</span><span>+</span></div>
  <div class="faq-row" style="top:258px"><span>Lorem ipsum dolor sit amet consectetur?</span><span>+</span></div>

  <p class="ticker"><span class="serif" style="margin-left:-3px">Mental Health</span><span class="star">✳</span>Get <span class="serif"><i>Dr. Jodel</i></span> Mind <span class="serif">Your Mental Health</span><span class="star">✳</span>Get</p>

  <svg class="abs" style="left:50px;top:345px" width="200" height="110" viewBox="0 0 200 110" aria-hidden="true">
    <path d="M20 90 Q60 10 150 15 Q195 20 180 50 Q150 80 60 100" fill="none" stroke="#3a5a48" stroke-width="1.2"/>
  </svg>
  <div class="photo" style="left:47px;top:377px;width:55px;height:65px;transform:rotate(-12deg);background:linear-gradient(160deg,#dcd6cf,#a9a29a)" role="img" aria-label="Photo of a smiling young woman"></div>
  <div class="photo" style="left:178px;top:382px;width:56px;height:66px;transform:rotate(10deg);background:linear-gradient(160deg,#b08a6c,#4a3a30)" role="img" aria-label="Photo of a smiling young man"></div>
  <div class="photo" style="left:112px;top:376px;width:79px;height:99px;background:linear-gradient(170deg,#d8c7a8,#b7936e 60%,#6c5a45)" role="img" aria-label="Photo of a calm woman with hair tied up"></div>

  <p class="join" style="top:497px">Join over MANY people<br>improving their health with <span style="font-family:var(--serif);font-size:11px">Dr. Jodel</span></p>
  <span class="btn" style="left:124px;top:527px;width:54px;height:18px">Contact us now</span>
</section>

</body>
</html>
```